Western Canadian Survey Company needs Business Card and Letter Head Design

Hello,

We're looking to have our business cards redesigned along with our letterhead.

We've recently changed out logo and would like to use this. Please use some creativity and propose different options (Traditional and modern).

We will provide as much feedback as possible.

Business card should be double sided with our logo. We would also like room for cell phone number, email address and position. Back of the card can just be our logo or potentially a list of our services we provide.

Industry/Entity Type

Business

Contact Information for Business Card

```html
<!DOCTYPE html>
<html lang="en">
<head>
<meta charset="utf-8">
<title>Ridgeline Field Surveys – Business Card</title>
<link rel="stylesheet" href="https://fonts.googleapis.com/css2?family=Open+Sans:wght@400;600;700&display=swap">
<style>
  :root {
    --backdrop: #2b2b2d;
    --card-black: #0c0c0d;
    --card-white: #f3f3f2;
    --steel: #7e90a4;
    --steel-light: #b9c4d0;
    --ink-grey: #5d5d60;
    --text-light: #c9c9cb;
    --icon-tile: #3a3a3d;
  }
  * { box-sizing: border-box; margin: 0; padding: 0; }
  html, body { width: 1200px; height: 900px; overflow: hidden; }
  body {
    background: var(--backdrop);
    font-family: "Open Sans", Arial, sans-serif;
    position: relative;
  }
  .card {
    position: absolute;
    left: 320px;
    width: 560px;
    height: 320px;
    overflow: hidden;
    box-shadow: 0 10px 30px rgba(0,0,0,0.45);
  }

  /* Shared wordmark */
  .wordmark {
    position: absolute;
    display: flex; flex-direction: column;
  }
  .wordmark .mark-row { display: flex; align-items: center; gap: 10px; }
  .wordmark .square { width: 14px; height: 14px; flex: none; }
  .wordmark .name {
    font-weight: 700; font-size: 22px; letter-spacing: 1.5px; line-height: 1.15;
  }
  .wordmark .rule { height: 2px; margin-top: 8px; align-self: stretch; }

  /* Back side */
  .card-back { top: 70px; background: var(--card-black); }
  .card-back .wordmark { left: 120px; top: 78px; align-items: flex-start; }
  .card-back .square { background: var(--steel-light); }
  .card-back .name { color: var(--steel-light); }
  .card-back .rule { background: var(--steel-light); }
  .card-back .web {
    position: absolute; left: 0; right: 0; top: 200px;
    text-align: center; color: var(--card-white);
    font-size: 14px; font-weight: 600;
  }
  .card-back .band {
    position: absolute; left: 0; right: 0; bottom: 0; height: 30px;
    background: var(--steel);
  }

  /* Front side */
  .card-front { top: 470px; background: var(--card-white); }
  .card-front .field { position: absolute; left: 0; top: 0; }
  .card-front .wordmark { right: 30px; top: 30px; align-items: flex-end; }
  .card-front .square { background: var(--steel); }
  .card-front .name { color: var(--steel); text-align: right; }
  .card-front .rule { background: var(--card-black); }

  .holder { position: absolute; left: 40px; top: 118px; }
  .holder .person {
    color: var(--steel); font-weight: 700; font-size: 19px; letter-spacing: 0.5px;
  }
  .holder .role { color: var(--ink-grey); font-size: 14px; margin-top: 2px; }

  .contact-list {
    position: absolute; left: 40px; top: 210px; list-style: none;
  }
  .contact-list li {
    display: flex; align-items: center; gap: 9px;
    color: var(--text-light); font-size: 13px; height: 22px;
  }
  .contact-list svg { width: 14px; height: 14px; flex: none; }

  .address {
    position: absolute; right: 30px; top: 160px;
    text-align: right; color: var(--text-light); font-size: 14px; line-height: 1.5;
  }
</style>
</head>
<body>

<section class="card card-back" aria-label="Business card, back">
  <div class="wordmark">
    <div class="mark-row">
      <span class="square"></span>
      <span class="name">RIDGELINE FIELD<br>SURVEYS LTD</span>
    </div>
    <span class="rule"></span>
  </div>
  <p class="web">www.ridgelinesurveys.net</p>
  <div class="band"></div>
</section>

<section class="card card-front" aria-label="Business card, front">
  <svg class="field" width="560" height="320" viewBox="0 0 560 320" aria-hidden="true">
    <polygon points="0,196 104,196 112,186 120,196 300,196 300,138 560,138 560,320 0,320" fill="var(--card-black)"/>
    <rect x="0" y="292" width="560" height="28" fill="var(--steel)"/>
  </svg>

  <div class="wordmark">
    <div class="mark-row">
      <span class="square"></span>
      <span class="name">RIDGELINE FIELD<br>SURVEYS LTD</span>
    </div>
    <span class="rule"></span>
  </div>

  <div class="holder">
    <p class="person">JORDAN WHITAKER</p>
    <p class="role">General Manager</p>
  </div>

  <ul class="contact-list">
    <li>
      <svg viewBox="0 0 14 14" aria-hidden="true"><rect width="14" height="14" rx="3" fill="var(--icon-tile)"/><path d="M4 3.5l1.6-.3.8 2-1 .8a5 5 0 0 0 2.6 2.6l.8-1 2 .8-.3 1.6C8 10.5 3.5 6 4 3.5z" fill="var(--text-light)"/></svg>
      +000 555 0148
    </li>
    <li>
      <svg viewBox="0 0 14 14" aria-hidden="true"><rect width="14" height="14" rx="3" fill="var(--icon-tile)"/><rect x="3" y="4.5" width="8" height="5.5" fill="none" stroke="var(--text-light)" stroke-width="1"/><path d="M3 4.5l4 3 4-3" fill="none" stroke="var(--text-light)" stroke-width="1"/></svg>
      hr@ridgelinesurveys.net
    </li>
    <li>
      <svg viewBox="0 0 14 14" aria-hidden="true"><rect width="14" height="14" rx="3" fill="var(--icon-tile)"/><circle cx="7" cy="7" r="3.6" fill="none" stroke="var(--text-light)" stroke-width="1"/><path d="M3.4 7h7.2M7 3.4c-1.6 2-1.6 5.2 0 7.2M7 3.4c1.6 2 1.6 5.2 0 7.2" fill="none" stroke="var(--text-light)" stroke-width="0.8"/></svg>
      www.ridgelinesurveys.net
    </li>
  </ul>

  <p class="address">218 Cedar Ridge Way<br>Larchmere, XX. A0A</p>
</section>

</body>
</html>
```